Anzeigengestaltung für Brötchen- und Brotlieferant
Zielgruppe
Wir beliefern Privatkunden Freitag, Samstag und Sonntag mit Brötchen / Broten und suchen ein Design für eine Werbekampagne zur Neukundengewinnung über Facebook. Sprich ein Bild indem alles kurz und knapp für den Kunden erklärt wird und man damit Werbung schalten kann.

```html
<!DOCTYPE html>
<html lang="de">
<head>
<meta charset="utf-8">
<title>Brötchenservice Kessing – Lieferung frischer Backwaren</title>
<link rel="stylesheet" href="https://fonts.googleapis.com/css2?family=Open+Sans:wght@400;700&display=swap">
<style>
  :root {
    --bg-dark: #2f2b27;
    --bg-wall: #4a4540;
    --crumb-light: #e2d5c3;
    --crumb-mid: #c4ad92;
    --crust: #8a5a36;
    --crust-dark: #5e3c24;
    --board: #9c6a42;
    --cloth: #d8c6bc;
    --band: rgba(255, 255, 255, 0.66);
    --brown: #5a4131;
    --text-grey: #4d4a47;
    --logo-peach: #f6c9a0;
    --logo-brown: #8c5a3c;
  }
  html, body {
    margin: 0;
    padding: 0;
    overflow: hidden;
  }
  .ad {
    position: relative;
    width: 1200px;
    height: 628px;
    overflow: hidden;
    font-family: "Open Sans", Arial, sans-serif;
  }
  .ad__photo {
    position: absolute;
    inset: 0;
    background:
      radial-gradient(ellipse 250px 120px at 590px 165px, var(--crumb-light) 0%, var(--crumb-mid) 60%, rgba(196,173,146,0) 100%),
      radial-gradient(ellipse 300px 150px at 590px 170px, var(--crust) 55%, rgba(138,90,54,0) 100%),
      radial-gradient(ellipse 190px 110px at 680px 520px, var(--crumb-light) 0%, var(--crumb-mid) 65%, rgba(196,173,146,0) 100%),
      radial-gradient(ellipse 330px 170px at 540px 480px, var(--crust) 0%, var(--crust-dark) 70%, rgba(94,60,36,0) 100%),
      radial-gradient(ellipse 380px 120px at 520px 600px, var(--board) 0%, rgba(156,106,66,0) 100%),
      radial-gradient(ellipse 140px 200px at 1090px 540px, #b48a60 0%, rgba(180,138,96,0) 100%),
      radial-gradient(ellipse 260px 180px at 180px 120px, #7d6a58 0%, rgba(125,106,88,0) 100%),
      radial-gradient(ellipse 260px 160px at 150px 540px, var(--cloth) 0%, rgba(216,198,188,0) 100%),
      radial-gradient(ellipse 300px 220px at 950px 450px, #cdbfb4 0%, rgba(205,191,180,0) 100%),
      linear-gradient(180deg, var(--bg-dark) 0%, var(--bg-wall) 40%, #8a7a6c 100%);
  }
  .ad__band {
    position: absolute;
    left: 0;
    top: 233px;
    width: 1200px;
    height: 202px;
    background: var(--band);
  }
  .brand {
    position: absolute;
    left: 25px;
    top: 254px;
    width: 224px;
    display: flex;
    flex-direction: column;
    align-items: center;
    gap: 4px;
    color: var(--logo-brown);
    font-weight: 400;
    font-size: 20px;
    line-height: 26px;
    text-align: center;
  }
  .headline {
    position: absolute;
    left: 200px;
    width: 800px;
    top: 240px;
    margin: 0;
    text-align: center;
    color: var(--brown);
    font-weight: 700;
    font-size: 43px;
    line-height: 54px;
  }
  .info {
    position: absolute;
    top: 372px;
    left: 288px;
    display: flex;
    gap: 40px;
    color: var(--text-grey);
    font-size: 22px;
  }
  .info__item {
    display: flex;
    align-items: center;
    gap: 10px;
  }
</style>
</head>
<body>
  <main class="ad">
    <div class="ad__photo" role="img" aria-label="Foto: Hände brechen ein frisches Sauerteigbrot über einem Laib auf einem Holzbrett auseinander"></div>
    <div class="ad__band"></div>

    <div class="brand">
      <span class="brand__title">Brötchenservice</span>
      <svg width="100" height="100" viewBox="0 0 100 100" aria-hidden="true">
        <circle cx="50" cy="50" r="48" fill="var(--logo-peach)"/>
      </svg>
      <span class="brand__name">Tobias Kessing</span>
    </div>

    <h1 class="headline">Wir liefern Ihnen frisches<br>Brot &amp; Brötchen nach Hause</h1>

    <div class="info">
      <div class="info__item">
        <svg width="30" height="30" viewBox="0 0 30 30" aria-hidden="true">
          <circle cx="15" cy="15" r="13" fill="none" stroke="var(--text-grey)" stroke-width="2.2"/>
          <path d="M15 7v8h6" fill="none" stroke="var(--text-grey)" stroke-width="2.2" stroke-linecap="round"/>
        </svg>
        <span>Freitags, Samstags &amp; Sonntags</span>
      </div>
      <div class="info__item">
        <svg width="26" height="32" viewBox="0 0 26 32" aria-hidden="true">
          <path d="M13 1C6.4 1 1 6.3 1 12.8 1 21.5 13 31 13 31s12-9.5 12-18.2C25 6.3 19.6 1 13 1z" fill="var(--brown)"/>
          <circle cx="13" cy="12.5" r="4.5" fill="#ece7e2"/>
        </svg>
        <span>11111 Musterstadt</span>
      </div>
    </div>
  </main>
</body>
</html>
```